Professional business cards for real estate development company

I need business cards for my new real estate development company. The company, "KORVA" is a real estate development, investment, and advisory firm with a focus on multifamily, office, and mixed-use projects across primary and secondary markets in the Southeast United States.

Style preference is modern

Industry/Entity Type

Real Estate Development

Contact Information for Business Card

The business cards need to include:
Name
Title
Mailing Address
Phone Number
Web Address

Logo is attached. I would like white to be the primary color with incorporation of the company colors: #232D3A and #B5A451

Font styles to use
Other font styles liked:
• Montserrat, Avenir

Requirements
Must have
• Company Logo. No need to include the company name since the name is in the logo.
Should not have
• No line type designs

```html
<!DOCTYPE html>
<html lang="en">
<head>
<meta charset="utf-8">
<title>KORVA Business Cards</title>
<link rel="stylesheet" href="https://fonts.googleapis.com/css2?family=Montserrat:wght@700&family=Ubuntu:wght@300;400;500&display=swap">
<style>
  :root {
    --navy: #232d3a;
    --backdrop: #212a38;
    --gold: #b5a451;
    --white: #ffffff;
    --soft-white: #e6e8ec;
  }
  html, body {
    margin: 0;
    padding: 0;
    width: 1200px;
    height: 1200px;
    overflow: hidden;
    background: var(--backdrop);
  }
  .canvas {
    position: relative;
    width: 1200px;
    height: 1200px;
  }
  .card {
    position: absolute;
    left: 197px;
    width: 814px;
    height: 492px;
    background: var(--white);
    box-shadow: -12px 22px 30px rgba(0, 0, 0, 0.45);
    overflow: hidden;
  }
  .card--front { top: 80px; }
  .card--back { top: 628px; }

  .front-panel {
    position: absolute;
    inset: 0;
  }
  .wordmark {
    position: absolute;
    font-family: 'Montserrat', sans-serif;
    font-weight: 700;
    color: var(--navy);
    letter-spacing: 0.04em;
    line-height: 1;
    text-align: center;
    transform: translateX(-50%);
    white-space: nowrap;
  }
  .card--front .wordmark {
    left: 219px;
    top: 206px;
    font-size: 78px;
  }
  .card--back .wordmark {
    left: 407px;
    top: 160px;
    font-size: 124px;
  }

  .identity {
    position: absolute;
    left: 443px;
    top: 76px;
    color: var(--white);
  }
  .identity__name {
    font-family: 'Montserrat', sans-serif;
    font-weight: 700;
    font-size: 37px;
    letter-spacing: 0.02em;
    line-height: 1;
    margin: 0;
  }
  .identity__title {
    font-family: 'Ubuntu', sans-serif;
    font-weight: 300;
    font-size: 28px;
    line-height: 1;
    margin: 6px 0 0;
    color: var(--soft-white);
  }

  .contacts {
    position: absolute;
    left: 0;
    top: 0;
    margin: 0;
    padding: 0;
    list-style: none;
  }
  .contact {
    position: absolute;
    left: 444px;
    display: flex;
    align-items: center;
    white-space: nowrap;
  }
  .contact__icon {
    width: 28px;
    height: 28px;
    flex: none;
  }
  .contact__text {
    margin-left: 9px;
    font-family: 'Ubuntu', sans-serif;
    font-weight: 400;
    font-size: 15.5px;
    line-height: 1.2;
    letter-spacing: 0.06em;
    color: var(--soft-white);
  }
  .contact--email { top: 258px; }
  .contact--phone { top: 294px; }
  .contact--web { top: 340px; }
  .contact--web .contact__text { letter-spacing: 0.12em; }

  .back-url {
    position: absolute;
    left: 0;
    right: 0;
    top: 406px;
    text-align: center;
    font-family: 'Ubuntu', sans-serif;
    font-weight: 500;
    font-size: 23px;
    letter-spacing: 0.03em;
    color: var(--navy);
  }
</style>
</head>
<body>
<main class="canvas">

  <section class="card card--front">
    <svg class="front-panel" width="814" height="492" viewBox="0 0 814 492" aria-hidden="true">
      <path fill="var(--navy)" d="M221 0 H814 V403 H490 A64 64 0 0 1 426 339 V220 C426 95 340 0 221 0 Z"/>
    </svg>

    <div class="wordmark">KORVA</div>

    <div class="identity">
      <p class="identity__name">JANATHAN DOE</p>
      <p class="identity__title">Job Tittle Here</p>
    </div>

    <ul class="contacts">
      <li class="contact contact--email">
        <svg class="contact__icon" viewBox="0 0 28 28" aria-hidden="true">
          <circle cx="14" cy="14" r="14" fill="var(--gold)"/>
          <path d="M7 9 L21 14 L12 20 L12 15 Z" fill="var(--white)"/>
        </svg>
        <span class="contact__text">BRAND-NAME@EMAIL.COM</span>
      </li>
      <li class="contact contact--phone">
        <svg class="contact__icon" viewBox="0 0 28 28" aria-hidden="true">
          <circle cx="14" cy="14" r="14" fill="var(--gold)"/>
          <path d="M7 11 Q14 6 21 11 L20 13 L17 12 L17 11 Q14 10 11 11 L11 12 L8 13 Z" fill="var(--white)"/>
          <rect x="9" y="14" width="10" height="6" rx="1" fill="var(--white)"/>
          <circle cx="14" cy="17" r="1.6" fill="var(--gold)"/>
        </svg>
        <span class="contact__text">+000 1234 5678 999<br>+012 9934 5271 003</span>
      </li>
      <li class="contact contact--web">
        <svg class="contact__icon" viewBox="0 0 28 28" aria-hidden="true">
          <circle cx="14" cy="14" r="14" fill="var(--gold)"/>
          <g fill="none" stroke="var(--white)" stroke-width="1.4">
            <circle cx="14" cy="14" r="7"/>
            <ellipse cx="14" cy="14" rx="3" ry="7"/>
            <line x1="7" y1="14" x2="21" y2="14"/>
          </g>
        </svg>
        <span class="contact__text">WWW.BRANDNAME.COM</span>
      </li>
    </ul>
  </section>

  <section class="card card--back">
    <div class="wordmark">KORVA</div>
    <p class="back-url">WWW.BRAND-NAME.COM</p>
  </section>

</main>
</body>
</html>
```